VelMarkory-Tagsworthly Partial Redesign - Web App

Are you able to apply your creativity to an existing layout? I’m convinced that even just a few touches can make a big difference to add personality and professionalism to a website design, and I’m looking for someone able to use existing ideas and bring them to the next level while keeping inside some given constraints.
The actual job is to improve an existing design concept and to apply it creatively to a landing page, a simple home page, and an older web app (single page website).
To help you start with a clear picture of the current situation and of my requirements, I created a detailed brief with screenshots, live examples, and complete instructions. You can find it attached to this job.
My tastes are inclined towards clean and simple designs. For this project I'm not looking for dazzling novelty, but for very solid craftsmanship. Are the right man - or woman - for the job?
Updates
I wanted to thank everybody who participated in this project. I made a choice, but also other designs were interesting. Hope to work with you another time.
Target Market(s)
Our main target is social media marketers and startuppers
Look and feel
Each slider illustrates characteristics of the customer's brand and the style your logo design should communicate.

```html
<!DOCTYPE html>
<html lang="en">
<head>
<meta charset="utf-8">
<title>Tagsworthly.me – explore the hashtagspace</title>
<link rel="stylesheet" href="https://fonts.googleapis.com/css2?family=Arimo:ital,wght@0,400;0,700;1,400&family=Noto+Serif:ital@1&display=swap">
<style>
:root{
  --header-bg:#1b1b1b;
  --band-top:#2f7bd6;
  --band-bottom:#0f4fae;
  --accent-blue:#1f86e0;
  --olive:#8a8a1a;
  --pro-green:#5fa36a;
  --text-dark:#333;
  --node-blue:#7cbaf8;
  --node-pink:#f0479a;
  --edge:#a58cb0;
  --label-navy:#0d1a4a;
  --footer-bg:#1c1c1c;
  --footer-text:#e6e6e6;
  --card-bg:#d3d3d3;
}
*{margin:0;padding:0;box-sizing:border-box}
html,body{width:1200px;height:1144px;overflow:hidden;background:#fff;font-family:"Arimo",Arial,sans-serif;color:var(--text-dark)}
.canvas{position:relative;width:1200px;height:1144px;overflow:hidden}
.abs{position:absolute}
.site-header{position:absolute;left:0;top:0;width:1200px;height:43px;background:linear-gradient(#2c2c2c,#111)}
.brand-mark{left:250px;top:15px;width:12px;height:12px;border:2px solid #fff}
.brand{left:274px;top:11px;color:#fff;font-weight:700;font-size:17px;white-space:nowrap}
.tagline{left:414px;top:13px;color:#fff;font-style:italic;font-size:14.5px;white-space:nowrap}
.nav a{position:absolute;top:15px;color:#ddd;font-weight:700;font-size:12px;text-decoration:none}
.user-btn{left:926px;top:6px;width:48px;height:30px;border-radius:4px;background:#0c0c0c;border:1px solid #444}
.data-band{position:absolute;left:0;top:43px;width:1200px;height:72px;background:linear-gradient(var(--band-top),var(--band-bottom))}
.band-title{color:#fff;font-weight:700;font-size:13px;white-space:nowrap}
.band-title span{color:var(--olive)}
.tab{position:absolute;top:35px;height:21px;display:flex;border:1px solid #aac;border-radius:2px;font-size:9px;overflow:hidden;white-space:nowrap}
.tab .name{background:#f6f6f6;color:#555;padding:0 6px;line-height:19px;flex:1;text-align:center}
.tab .badge{background:var(--accent-blue);color:#fff;width:36px;text-align:center;line-height:19px;flex:none}
.tab .badge.pro{background:var(--pro-green)}
.search-input{left:751px;top:34px;width:155px;height:23px;border-radius:10px;background:#fff;border:1px solid #9bc}
.search-btn{left:915px;top:36px;width:60px;height:21px;border-radius:8px;background:var(--accent-blue);color:#fff;font-size:9.5px;font-weight:700;text-align:center;line-height:21px}
h2.section-title{position:absolute;top:141px;font-size:14.5px;font-weight:700;color:#333;white-space:nowrap}
.graph{left:200px;top:128px}
.info-bar{left:216px;top:173px;width:335px;height:31px;border:1px solid #8bbbe8;border-radius:3px;background:linear-gradient(#cfe6fb,#8fc4f6);font-size:10px;color:#245;line-height:29px;padding-left:30px;white-space:nowrap}
.info-bar .i{position:absolute;left:12px;top:0;font-style:italic;font-weight:700;font-family:"Noto Serif",serif;color:#246}
.info-bar .x{position:absolute;right:8px;top:9px;width:11px;height:11px;border-radius:50%;background:#7a9cc0}
.mode{top:684px;height:26px;font-size:10.5px;line-height:26px;text-align:center}
.mode.simple{left:379px;width:101px;background:var(--accent-blue);color:#fff;border-radius:2px 0 0 2px}
.mode.advanced{left:480px;width:100px;background:#f2f2f2;color:#777;border:1px solid #ccc}
.find-text{left:300px;width:360px;top:724px;text-align:center;font-size:11px;color:#222}
.pro-btn{left:370px;top:746px;width:222px;height:30px;background:var(--accent-blue);border:1px solid #0b5aaa;border-radius:2px;color:#fff;font-size:12.5px;text-align:center;line-height:28px;white-space:nowrap}
.tweet{position:absolute;left:762px;width:220px;height:76px;background:linear-gradient(#eaeaea,var(--card-bg));border:1px solid #bbb;border-radius:2px;box-shadow:0 1px 2px rgba(0,0,0,.25)}
.tweet .avatar{position:absolute;left:-6px;top:14px;width:50px;height:46px;background:linear-gradient(#b8a896,#6d6258);border:2px solid #fff;box-shadow:0 1px 2px rgba(0,0,0,.4)}
.tweet p{position:absolute;left:50px;top:13px;width:168px;font-family:"Noto Serif",serif;font-style:italic;font-size:9.5px;line-height:16px;color:#333}
.tweet p .handle{color:var(--accent-blue)}
.tweet p .tag{color:#666}
.tweet .time{position:absolute;left:62px;top:46px;font-size:9px;color:#aaa}
.tweet .time::before{content:"";position:absolute;left:-12px;top:2px;width:8px;height:7px;border-radius:50%;background:#bbb}
.site-footer{position:absolute;left:0;top:820px;width:1200px;height:324px;background:radial-gradient(ellipse at 50% 0,#2e2e2e,var(--footer-bg) 70%);border-top:4px solid #444;color:var(--footer-text);overflow:hidden}
.site-footer h3{position:absolute;top:20px;font-weight:400;font-size:18px;color:#fff}
.site-footer hr{position:absolute;top:50px;width:230px;border:0;border-top:1px solid #3a3a3a}
.contact-row{position:absolute;left:256px;font-size:11.5px;color:#fff;white-space:nowrap}
.contact-icon{position:absolute;left:229px;width:12px;height:10px;background:#ccc;border-radius:2px}
.about-name{left:486px;top:86px;font-size:13px;font-weight:700;color:#ddd}
.about-text{font-size:11px;line-height:17.6px;letter-spacing:.3px;color:#ddd}
.field{position:absolute;left:744px;width:232px;background:#161616;border:1px solid #2e2e2e;border-radius:3px;font-size:9.5px;color:#ddd;padding:8px 14px}
.required{left:748px;top:242px;font-size:9.5px;color:#fff}
.send-btn{left:925px;top:239px;width:50px;height:18px;background:#2a6fc9;color:#fff;font-size:10px;text-align:center;line-height:18px;border-radius:2px}
.legal-bar{position:absolute;left:0;top:284px;width:1200px;height:36px;border-top:1px solid #2f2f2f;font-size:8px;color:#999}
.legal-bar nav{position:absolute;right:225px;top:17px;white-space:nowrap}
.legal-bar nav span{margin:0 6px}
</style>
</head>
<body>
<div class="canvas">
<header class="site-header">
  <span class="abs brand-mark"></span>
  <div class="abs brand">Tagsworthly.me</div>
  <div class="abs tagline">explore the hashtagspace</div>
  <nav class="nav"><a style="left:737px">Blog</a><a style="left:796px">About</a><a style="left:864px">Help</a></nav>
  <div class="abs user-btn">
    <svg width="48" height="30" viewBox="0 0 48 30"><circle cx="18" cy="11" r="4" fill="#fff"/><path d="M11 22c0-5 14-5 14 0z" fill="#fff"/><path d="M31 12h8l-4 5z" fill="#fff"/></svg>
  </div>
</header>

<section class="data-band">
  <div class="abs band-title" style="left:223px;top:14px">Data for <span>#Hollywood</span></div>
  <div class="tab" style="left:224px;width:139px"><span class="name">Top Related Hashtag</span><span class="badge">FREE</span></div>
  <div class="tab" style="left:370px;width:116px"><span class="name">Top Influencers</span><span class="badge">FREE</span></div>
  <div class="tab" style="left:494px;width:83px"><span class="name">Varians</span><span class="badge">FREE</span></div>
  <div class="tab" style="left:585px;width:140px"><span class="name">In-Depth Intellegence</span><span class="badge pro">PRO</span></div>
  <div class="abs band-title" style="left:751px;top:14px">Popularity <span>65.9</span></div>
  <div class="abs search-input"></div>
  <div class="abs search-btn">SEARCH</div>
</section>

<h2 class="section-title" style="left:216px">The TOP 10 related hashtags for #hollywood</h2>

<svg class="abs graph" width="560" height="560" viewBox="250 160 700 700" font-family="Arimo,Arial,sans-serif" font-size="9" fill="#fff">
  <g stroke="var(--edge)">
    <line x1="595" y1="535" x2="486" y2="305" stroke-width="5"/>
    <line x1="595" y1="535" x2="692" y2="270" stroke-width="2"/>
    <line x1="595" y1="535" x2="363" y2="425" stroke-width="2"/>
    <line x1="595" y1="535" x2="676" y2="432" stroke-width="7"/>
    <line x1="595" y1="535" x2="870" y2="416" stroke-width="3"/>
    <line x1="595" y1="535" x2="318" y2="580" stroke-width="4"/>
    <line x1="595" y1="535" x2="866" y2="591" stroke-width="6"/>
    <line x1="595" y1="535" x2="434" y2="701" stroke-width="2"/>
    <line x1="595" y1="535" x2="754" y2="716" stroke-width="7"/>
    <line x1="595" y1="535" x2="589" y2="782" stroke-width="4"/>
  </g>
  <g fill="var(--node-blue)">
    <circle cx="486" cy="305" r="68"/><circle cx="692" cy="270" r="55"/><circle cx="363" cy="425" r="45"/>
    <circle cx="676" cy="432" r="53"/><circle cx="870" cy="416" r="57"/><circle cx="318" cy="580" r="57"/>
    <circle cx="866" cy="591" r="52"/><circle cx="434" cy="701" r="47"/><circle cx="754" cy="716" r="46"/>
    <circle cx="589" cy="782" r="61"/>
  </g>
  <circle cx="595" cy="535" r="47" fill="var(--node-pink)"/>
  <g fill="var(--label-navy)">
    <rect x="444" y="299" width="84" height="16" rx="2"/><rect x="668" y="265" width="48" height="16" rx="2"/>
    <rect x="347" y="420" width="32" height="16" rx="2"/><rect x="658" y="427" width="36" height="16" rx="2"/>
    <rect x="829" y="410" width="82" height="16" rx="2"/><rect x="297" y="575" width="42" height="16" rx="2"/>
    <rect x="852" y="586" width="28" height="16" rx="2"/><rect x="415" y="696" width="38" height="16" rx="2"/>
    <rect x="733" y="711" width="42" height="16" rx="2"/><rect x="569" y="777" width="40" height="16" rx="2"/>
    <rect x="568" y="530" width="54" height="16" rx="2"/>
  </g>
  <g text-anchor="middle">
    <text x="486" y="312">teamfollowback</text><text x="692" y="278">fashion</text><text x="363" y="433">retail</text>
    <text x="676" y="440">sexy</text><text x="870" y="423">autofollowback</text><text x="318" y="588">music</text>
    <text x="866" y="599">hot</text><text x="434" y="709">sales</text><text x="754" y="724">gossip</text>
    <text x="589" y="790">news</text><text x="595" y="543">celebrity</text>
  </g>
</svg>

<div class="abs info-bar"><span class="i">i</span>To explore the hashtag, click on the balls<span class="x"></span></div>

<div class="abs mode simple">Simple Mode</div>
<div class="abs mode advanced">Advanced Mode</div>
<div class="abs find-text">Find all trending related hashtags for #tag with</div>
<div class="abs pro-btn">VelMarkory Hashtag Intelligence Pro</div>

<h2 class="section-title" style="left:759px">TOP RECENT TWEETS</h2>
<div class="tweet" style="top:174px"><div class="avatar" role="img" aria-label="Author profile photo"></div><p>Maria Vance and Sola Reyes have a mustard-off <span class="handle">@ravelbor</span> <span class="tag">#hollywood</span></p><span class="time">2 hours ago</span></div>
<div class="tweet" style="top:262px"><div class="avatar" role="img" aria-label="Author profile photo"></div><p>Maria Vance and Sola Reyes have a mustard-off <span class="handle">@ravelbor</span> <span class="tag">#hollywood</span></p><span class="time">2 hours ago</span></div>
<div class="tweet" style="top:351px"><div class="avatar" role="img" aria-label="Author profile photo"></div><p>Maria Vance and Sola Reyes have a mustard-off <span class="handle">@ravelbor</span> <span class="tag">#hollywood</span></p><span class="time">2 hours ago</span></div>
<div class="tweet" style="top:440px"><div class="avatar" role="img" aria-label="Author profile photo"></div><p>Maria Vance and Sola Reyes have a mustard-off <span class="handle">@ravelbor</span> <span class="tag">#hollywood</span></p><span class="time">2 hours ago</span></div>
<div class="tweet" style="top:528px"><div class="avatar" role="img" aria-label="Author profile photo"></div><p>Maria Vance and Sola Reyes have a mustard-off <span class="handle">@ravelbor</span> <span class="tag">#hollywood</span></p><span class="time">2 hours ago</span></div>
<div class="tweet" style="top:617px"><div class="avatar" role="img" aria-label="Author profile photo"></div><p>Maria Vance and Sola Reyes have a mustard-off <span class="handle">@ravelbor</span> <span class="tag">#hollywood</span></p><span class="time">2 hours ago</span></div>
<div class="tweet" style="top:705px"><div class="avatar" role="img" aria-label="Author profile photo"></div><p>Maria Vance and Sola Reyes have a mustard-off <span class="handle">@ravelbor</span> <span class="tag">#hollywood</span></p><span class="time">2 hours ago</span></div>

<footer class="site-footer">
  <h3 style="left:228px">Reach Us</h3><hr style="left:228px">
  <h3 style="left:486px">About Us</h3><hr style="left:486px">
  <h3 style="left:744px;top:22px">Contact Us</h3><hr style="left:744px;top:52px">

  <span class="contact-icon" style="top:74px"></span><div class="contact-row" style="top:72px">info@velmarkory.com</div>
  <svg class="abs" style="left:229px;top:96px" width="12" height="12" viewBox="0 0 12 12"><path d="M2 1l3 0 1 3-2 1c1 2 2 3 4 4l1-2 3 1 0 3c-6 0-10-4-10-10z" fill="#ccc"/></svg>
  <div class="contact-row" style="top:96px">123-456-7890</div>
  <svg class="abs" style="left:229px;top:119px" width="13" height="12" viewBox="0 0 13 12"><path d="M6.5 0L13 6h-2v6H8V8H5v4H2V6H0z" fill="#ccc"/></svg>
  <div class="contact-row" style="top:120px">Somewhere street 12</div>
  <div class="contact-row" style="top:144px">City Name</div>
  <div class="contact-row" style="top:168px">Country Name, 12345</div>
  <span class="contact-icon" style="top:194px;border-radius:50%"></span><div class="contact-row" style="top:192px">@velmarkory</div>
  <span class="contact-icon" style="top:218px;width:11px;height:11px"></span><div class="contact-row" style="top:216px">social.velmarkory.com</div>

  <div class="abs about-name">VelMarkory</div>
  <div class="abs about-text" style="left:580px;top:61px;width:140px">Lorem ipsum dolor sit amet, consectetuer adipiscing elit, sed diam nonummy nibh euismod</div>
  <div class="abs about-text" style="left:482px;top:131px;width:240px">Lorem ipsum dolor sit amet, consectetuer adipiscing elit, sed diam nonummy nibh euismod tincidunt ut laoreet dolore magna aliquam erat volutpat. Ut wisi enim ad minim veniam, quis nostrud exerci tation ullamcor-per suscipit lobortis nisl ut aliquip ex ea</div>

  <div class="field" style="top:66px;height:24px;padding-top:6px">your name</div>
  <div class="field" style="top:100px;height:24px;padding-top:6px">your email</div>
  <div class="field" style="top:136px;height:97px">your message</div>
  <div class="abs required">* All Fields Are Required</div>
  <div class="abs send-btn">SEND</div>

  <div class="legal-bar">
    <span class="abs" style="left:226px;top:17px">Copyright @ 2012 VelMarkory</span>
    <nav>About Us<span>|</span>Programs<span>|</span>Services<span>|</span>Contact</nav>
  </div>
</footer>
</div>
</body>
</html>
```